Industrial Laundry News Paper Add

We need a color add for 1/4 page newspaper using blue and white. We are an industrial laundry providing linen washing for condo rental companies. We can provide linen rental and wash customer-owned goods

```html
<!DOCTYPE html>
<html lang="en">
<head>
<meta charset="utf-8">
<title>Summit Ridge Services – Commercial Laundry Ad</title>
<link rel="stylesheet" href="https://fonts.googleapis.com/css2?family=Raleway:wght@400;500;600;700;800&display=swap">
<style>
  :root {
    --navy: #1e1a4f;
    --steel-blue: #5871a6;
    --white: #ffffff;
    --ink: #1b1b24;
    --backdrop: #e9eaec;
  }
  * { box-sizing: border-box; margin: 0; padding: 0; }
  html, body {
    width: 1045px; height: 1200px; overflow: hidden;
    background: var(--backdrop);
    font-family: "Raleway", sans-serif;
  }
  .ad {
    position: absolute; left: 138px; top: 0;
    width: 689px; height: 1076px;
    transform: scale(1.1152); transform-origin: 0 0;
    background: var(--white); overflow: hidden;
  }
  .ad-shapes, .ad-photo { position: absolute; left: 0; top: 0; width: 689px; height: 1076px; }
  .call-us {
    position: absolute; right: 21px; top: 34px;
    color: var(--white); text-align: right;
    font-size: 17px; font-weight: 600; line-height: 23px;
  }
  .brand {
    position: absolute; right: 38px; top: 548px;
    display: flex; align-items: center; gap: 10px;
    color: #24409a; font-size: 21px; font-weight: 700; letter-spacing: 0.2px;
  }
  .brand-dot { width: 14px; height: 14px; border-radius: 50%; background: var(--steel-blue); }
  .headline {
    position: absolute; right: 34px; top: 610px;
    text-align: right; color: var(--navy);
    font-size: 38px; font-weight: 800; line-height: 50px; letter-spacing: 0.3px;
  }
  .about {
    position: absolute; left: 43px; top: 736px; width: 375px;
    color: var(--ink); font-size: 16.5px; font-weight: 500; line-height: 22px;
  }
  .quote-bubble {
    position: absolute; left: 455px; top: 737px; width: 200px; height: 200px;
    border-radius: 50%; background: var(--navy); color: var(--white);
    display: flex; flex-direction: column; align-items: center; justify-content: center;
    text-align: center; font-size: 16px; font-weight: 700; line-height: 22px;
    padding-top: 6px;
  }
  .quote-bubble svg { margin-bottom: 6px; }
  .contact-bar {
    position: absolute; left: 0; top: 980px; width: 689px; height: 26px;
    background: var(--steel-blue); color: var(--white);
    font-size: 16px; font-weight: 700; padding: 3px 0 0 43px;
  }
  .footer {
    position: absolute; left: 0; top: 1006px; width: 689px; height: 70px;
    background: var(--navy); color: var(--white);
  }
  .footer-details {
    position: absolute; left: 43px; top: 16px;
    font-size: 14.5px; font-weight: 500; line-height: 19px;
  }
  .follow {
    position: absolute; right: 33px; top: 6px; text-align: center;
    font-size: 16px; font-weight: 700;
  }
  .social { display: flex; gap: 5px; justify-content: center; margin-top: 6px; }
  .social span { width: 19px; height: 19px; border-radius: 50%; background: var(--white); }
</style>
</head>
<body>
  <main class="ad">
    <svg class="ad-photo" viewBox="0 0 689 1076" role="img" aria-label="Photo of a row of stainless steel front-loading commercial washing machines">
      <defs>
        <linearGradient id="washer-tones" x1="0" y1="0" x2="1" y2="1">
          <stop offset="0" stop-color="#b9bcc2"/>
          <stop offset="0.45" stop-color="#7f93a8"/>
          <stop offset="1" stop-color="#c9cbcf"/>
        </linearGradient>
      </defs>
      <polygon points="0,0 689,0 689,430 292,515 0,440" fill="url(#washer-tones)"/>
    </svg>

    <svg class="ad-shapes" viewBox="0 0 689 1076" aria-hidden="true">
      <polygon points="420,0 689,0 689,190" fill="var(--steel-blue)"/>
      <polygon points="367,0 420,0 689,190 689,205" fill="var(--navy)"/>
      <polygon points="352,0 367,0 689,205 689,235" fill="var(--white)"/>
      <polygon points="0,440 292,515 0,575" fill="var(--navy)"/>
      <polygon points="0,575 689,430 689,452 0,612" fill="var(--steel-blue)"/>
      <circle cx="600" cy="765" r="60" fill="var(--steel-blue)"/>
      <circle cx="477" cy="905" r="37" fill="var(--steel-blue)"/>
    </svg>

    <p class="call-us">CALL US:<br>+1.5550142800</p>

    <div class="brand"><span class="brand-dot"></span>SUMMIT RIDGE SERVICES</div>

    <h1 class="headline">PINE HOLLOW'S NEWEST<br>COMMERCIAL LAUNDRY</h1>

    <p class="about">Summit Ridge Services is a family-owned and operated service company. Our commitment is to continued growth by offering customers a consistent, reliable total cleaning solution day in and day out. We always strive to combine industry experience with the latest cleaning technologies and environmentally friendly products - so you get the best possible results.</p>

    <div class="quote-bubble">
      <svg width="40" height="38" viewBox="0 0 40 38" aria-hidden="true">
        <path d="M4 12 Q16 4 28 12 L26 17 L21 16 L20 13 Q16 12 12 13 L11 16 L6 17 Z" fill="var(--white)"/>
        <path d="M9 19 H23 L26 34 H6 Z" fill="var(--white)"/>
        <g fill="var(--navy)">
          <rect x="11" y="24" width="3" height="2"/><rect x="15" y="24" width="3" height="2"/><rect x="19" y="24" width="3" height="2"/>
          <rect x="11" y="28" width="3" height="2"/><rect x="15" y="28" width="3" height="2"/><rect x="19" y="28" width="3" height="2"/>
        </g>
        <path d="M31 8 Q34 11 31 14 M34 5 Q39 11 34 17" stroke="var(--white)" stroke-width="2" fill="none" stroke-linecap="round"/>
      </svg>
      You like it clean<br>we like it dirty,<br>call us for a quote<br>+1.5550142800
    </div>

    <div class="contact-bar">CONTACT US FOR MORE INFORMATION</div>

    <footer class="footer">
      <p class="footer-details">+1.5550142800 &nbsp;|&nbsp; www.summitridgeservices.com<br>Granite Peak Partners, Inc. Pine Hollow, CA 90000, USA</p>
      <div class="follow">FOLLOW US
        <div class="social"><span></span><span></span><span></span></div>
      </div>
    </footer>
  </main>
</body>
</html>
```